Home page web design for "Tales from Tamsin"

We need a home page web design for a start up company that will write memoirs for seniors.
The completed project will need to include PSD files...NO HTML or CSS necessary.
Attached is a brief outline concept that may give you some ideas...but you are the creative professionals, so please feel free to add your ideas. We will also attach some files that show you our logo, brochures, and photos that could be used to give you ideas of our focus.
There will need to be access to the other pages on the home page to include: 'About Us'; 'How We Can Help'; 'Community Sessions'; 'Senior Consulting ' and 'Contact Us'.
Updates

Project Deadline Extended Reason: We want designers to have sufficient time to get all their proposals and revisions submitted. THANK YOU Added Wednesday, October 15, 2014

Target Market(s)

Seniors and Baby Boomers

Industry/Entity Type

It Company

Number of Pages Required

1 page

Colors
f9ba93
fbca95
faa54b
faf289
f37123

Requirements
Must have
• Script easy on senior eyes.
• Initial contact number would be 844-4LEGACY
Nice to have
• While the color pallet is non-specific we prefer the warm colors.
• salmon, peach.......
• NOT so much the orange of Halloween:)
• However, please utilize your creativity and put in colors you feel will draw best with your design.

```html
<!DOCTYPE html>
<html lang="en">
<head>
<meta charset="utf-8">
<title>Tales from Tamsin – Home</title>
<link href="https://fonts.googleapis.com/css2?family=Oswald:wght@400&family=Yesteryear&display=swap" rel="stylesheet">
<style>
  :root {
    --peach: #fbca95;
    --orange: #f37123;
    --orange-text: #e8661c;
    --yellow-line: #faf289;
    --grey-line: #dcdcdc;
    --ink: #111111;
    --photo-warm: #8a5a3a;
    --photo-sea: #8fa3ad;
    --photo-dark: #3a3530;
  }
  * { box-sizing: border-box; margin: 0; padding: 0; }
  html, body { width: 1063px; height: 1200px; overflow: hidden; background: #fff; }
  body { position: relative; font-family: Arial, Helvetica, sans-serif; color: var(--ink); }

  .brand {
    position: absolute; top: 90px; left: 0; width: 1063px;
    text-align: center;
    font-family: "Oswald", sans-serif; font-weight: 400;
    font-size: 46px; line-height: 60px; color: var(--orange); letter-spacing: 1px;
  }
  .contact-number {
    position: absolute; top: 162px; left: 0; width: 1063px;
    text-align: center;
    font-family: "Oswald", sans-serif; font-weight: 400;
    font-size: 20px; line-height: 28px; color: var(--ink); letter-spacing: 1px;
  }

  .main-nav {
    position: absolute; top: 273px; left: 110px; width: 844px; height: 42px;
    border-top: 2px solid var(--yellow-line);
    border-bottom: 2px solid var(--grey-line);
    display: flex; justify-content: space-between; align-items: center;
    padding: 0 11px;
    font-family: "Oswald", sans-serif; font-size: 22px;
  }
  .main-nav a { color: var(--ink); text-decoration: none; white-space: nowrap; }
  .main-nav a.current { color: var(--orange); }

  .panel {
    position: absolute; top: 350px; left: 126px; width: 830px; height: 793px;
    background: var(--peach);
  }
  .panel::before, .panel::after {
    content: ""; position: absolute; left: 0; width: 100%; height: 5px;
  }
  .panel::before {
    top: -5px;
    background:
      linear-gradient(-45deg, var(--peach) 3.5px, transparent 0),
      linear-gradient(45deg, var(--peach) 3.5px, transparent 0);
    background-size: 7px 5px; background-position: left bottom;
  }
  .panel::after {
    bottom: -5px;
    background:
      linear-gradient(-135deg, var(--peach) 3.5px, transparent 0),
      linear-gradient(135deg, var(--peach) 3.5px, transparent 0);
    background-size: 7px 5px; background-position: left top;
  }

  .headline {
    position: absolute; top: 388px; left: 126px; width: 830px; text-align: center;
    font-family: "Yesteryear", cursive; font-size: 34px; font-weight: 400;
  }

  .intro {
    position: absolute; top: 466px; left: 234px; width: 590px;
    text-align: center; font-size: 12.5px; line-height: 20.3px;
  }
  .intro p { margin-bottom: 20.3px; }
  .intro .lead { color: var(--orange-text); font-weight: bold; }

  .cta {
    position: absolute; top: 880px; display: flex; align-items: center; gap: 8px;
    font-family: "Yesteryear", cursive; font-size: 34px; color: var(--ink); text-decoration: none;
    white-space: nowrap;
  }
  .cta-gifts { left: 383px; }
  .cta-learn { left: 707px; }

  .photo { position: absolute; border-radius: 50%; border: 6px solid var(--orange); background: #fff; padding: 4px; }
  .photo span { display: block; width: 100%; height: 100%; border-radius: 50%; }
  .photo-writing { left: 847px; top: 464px; width: 212px; height: 212px; }
  .photo-writing span { background: radial-gradient(circle at 60% 40%, #c99a74, var(--photo-warm) 55%, #3d2616); }
  .photo-beach { left: 90px; top: 843px; width: 218px; height: 218px; }
  .photo-beach span { background: linear-gradient(#b9c8c9, var(--photo-sea) 55%, #5e5a52 75%, #3e3a34); }
  .photo-book { left: 812px; top: 962px; width: 204px; height: 204px; }
  .photo-book span { background: radial-gradient(circle at 45% 50%, #7a6d66, var(--photo-dark) 65%, #15120f); }

  .footer {
    position: absolute; top: 1169px; left: 0; width: 1063px; text-align: center; font-size: 11px;
  }
  .footer strong { color: var(--orange); }
</style>
</head>
<body>
  <header class="brand">Tales from Tamsin</header>
  <p class="contact-number">844-4LEGACY</p>

  <nav class="main-nav">
    <a class="current" href="#">About Us</a>
    <a href="#">How We Can Help</a>
    <a href="#">Community Sessions</a>
    <a href="#">Senior Consulting Services</a>
    <a href="#">Contact Us</a>
  </nav>

  <section class="panel"></section>

  <h1 class="headline">When a genealogy doesn’t say enough!</h1>

  <div class="intro">
    <p class="lead">If you were alive in 100 years, what would you share with your descendants?</p>
    <p class="lead">Now you have a vehicle to help you immortalize your thoughts for the future…specifically for those who will want to know!</p>
    <p>We are not all presidents of countries or CEO’s of fortune 500 companies! But “every life legacy is a gift to be treasured by the next generation.”</p>
    <p>Does your family host generations of soldiers, doctors, farmers, scientists, mechanics, entrepreneurs, writers, politicians, contractors, pastors, artisans, athletes, musicians, etc..? Generational patterns can often emerge when writing your story that will interest the next generation.</p>
    <p>A genealogy, while very relevant, doesn’t offer the personal story of the names we find. A biography can place a deeper relevance on the face for future descendants. Every life is a legacy to pass forward and we at Tales from Tamsin believe everyone should chronicle their life journey in writing. This commitment allows you to be remembered for who you truly are as a person.</p>
    <p>Think about it….Do you know the triumphs and tribulations of your ancestors? Do you wish you did? Well, so will those falling into your personal family tree.</p>
  </div>

  <a class="cta cta-gifts" href="#">
    <svg width="56" height="56" viewBox="0 0 56 56" aria-hidden="true">
      <g fill="var(--orange)">
        <rect x="10" y="6" width="4" height="12"/><rect x="26" y="6" width="4" height="12"/><rect x="42" y="6" width="4" height="12"/>
        <path d="M4 22h48v12c-4 4-8 4-12 0-4 4-8 4-12 0-4 4-8 4-12 0-4 4-8 4-12 0z"/>
        <path d="M4 40c4 3 8 3 12 0 4 3 8 3 12 0 4 3 8 3 12 0 4 3 8 3 12 0v12H4z"/>
      </g>
    </svg>
    Great Gift Ideas
  </a>

  <a class="cta cta-learn" href="#">
    <svg width="54" height="56" viewBox="0 0 54 56" aria-hidden="true">
      <g fill="var(--orange)">
        <path d="M12 2h38l-6 44H6z"/>
        <path d="M4 48h40l-2 6H2z"/>
      </g>
      <g fill="var(--peach)">
        <rect x="18" y="12" width="22" height="4" transform="skewX(-8)"/>
        <rect x="18" y="20" width="22" height="4" transform="skewX(-8)"/>
      </g>
    </svg>
    Learn More
  </a>

  <div class="photo photo-writing"><span role="img" aria-label="Photo of an elderly woman writing at a lamp-lit desk"></span></div>
  <div class="photo photo-beach"><span role="img" aria-label="Photo of an older couple walking along a beach at dusk"></span></div>
  <div class="photo photo-book"><span role="img" aria-label="Photo of an older man holding up his finished memoir book"></span></div>

  <footer class="footer">© <strong>Tales from Tamsin</strong> - 2014. All Rights Reserved.</footer>
</body>
</html>
```